Wirenexa

I'm looking to much improve our current website wirenexa.com
Updates

Low design quality

Target Market(s)

Commercial clients (Not-Residentials)

Industry/Entity Type

Office buildings and Industrial clients

Coding

Coded - Design and coding required

Number of Pages Required

5+ page

Requirements
Must have
• Very professional structured low voltage cabling projects for Wi-Fi, Audio/Video conference rooms, Access Control systems, CCTV.

```html
<!DOCTYPE html>
<html lang="en">
<head>
<meta charset="utf-8">
<title>Wirenexa — Commercial Low Voltage Specialists</title>
<link rel="stylesheet" href="https://fonts.googleapis.com/css2?family=Archivo:wght@600;700;800&family=Inter:wght@400;500;600;700&display=swap">
<style>
:root{
  --red:#d8322c;
  --ink:#141414;
  --body:#5d5a58;
  --muted:#7a7674;
  --line:#e8e3df;
  --warm:#f7f3f1;
  --white:#ffffff;
}
*{box-sizing:border-box;margin:0;padding:0}
html,body{width:1200px;height:4817px;overflow:hidden}
body{font-family:"Inter",sans-serif;color:var(--ink);background:var(--white);font-size:13px;line-height:1.55}
h1,h2,h3,h4{font-family:"Archivo",sans-serif;color:var(--ink);letter-spacing:-.01em}
.wrap{width:904px;margin:0 auto;position:relative;height:100%}
.eyebrow{font-size:9px;font-weight:700;color:var(--red);text-transform:uppercase;letter-spacing:.04em}
.eyebrow.dark{color:var(--body)}
section{position:relative}

/* header */
.site-header{height:69px;border-bottom:1px solid var(--line);background:var(--white)}
.site-header .wrap{display:flex;align-items:center;justify-content:space-between}
.brand{display:flex;align-items:center;gap:8px;font-family:"Archivo",sans-serif;font-weight:800;font-size:34px;color:var(--ink);letter-spacing:-.02em}
.brand .mark{width:34px;height:34px;background:var(--red);border-radius:3px}
.nav{display:flex;gap:28px;font-size:11px;font-weight:600}
.nav .tel{color:var(--red)}

/* hero */
.hero{height:829px;background:var(--warm)}
.hero .eyebrow{position:absolute;top:75px;left:0}
.hero h1{position:absolute;top:96px;left:0;width:440px;font-size:64px;line-height:73px;font-weight:800}
.hero .lede{position:absolute;top:548px;left:0;width:385px;font-size:13px;line-height:21px;color:var(--body)}
.hero .actions{position:absolute;top:664px;left:0;display:flex;gap:10px}
.btn{display:inline-flex;align-items:center;gap:8px;height:35px;padding:0 16px;border-radius:4px;font-size:12px;font-weight:700}
.btn.primary{background:var(--red);color:#fff}
.btn.ghost{background:#fff;border:1px solid var(--line);color:var(--ink)}
.hero .tags{position:absolute;top:731px;left:0;display:flex;gap:8px}
.tag{height:23px;padding:0 10px;border:1px solid var(--line);border-radius:12px;background:#fff;font-size:10px;font-weight:600;display:flex;align-items:center}
.hero .photo{position:absolute;top:170px;left:435px;width:470px;height:485px;border-radius:6px;background:linear-gradient(160deg,#dcd8d3 0%,#f2efec 45%,#bdb5ad 100%);box-shadow:0 18px 40px rgba(0,0,0,.14)}

/* strip */
.strip{height:108px;border-top:1px solid var(--line);border-bottom:1px solid var(--line)}
.strip .wrap{display:flex}
.strip .cell{padding:26px 0 0 0;flex:1}
.strip .cell+.cell{border-left:1px solid var(--line);padding-left:24px}
.strip h4{font-family:"Inter",sans-serif;font-size:11px;font-weight:700;margin-bottom:6px}
.strip p{font-size:10.5px;line-height:18px;color:var(--muted);width:250px}

/* services */
.services{height:835px}
.center{text-align:center}
.services .eyebrow{position:absolute;top:75px;width:100%}
.services h2{position:absolute;top:95px;width:100%;font-size:44px;line-height:49px;font-weight:700}
.services .intro{position:absolute;top:262px;left:200px;width:504px;font-size:11.5px;line-height:20px;color:var(--body)}
.grid4{position:absolute;top:333px;left:0;width:904px;display:grid;grid-template-columns:repeat(4,1fr);gap:15px 14px}
.card{border:1px solid var(--line);border-radius:6px;background:#fff;padding:20px 18px}
.grid4 .card:nth-child(-n+4){height:217px}
.grid4 .card:nth-child(n+5){height:200px}
.icon{width:28px;height:28px;border-radius:5px;background:#fbe9e8;display:flex;align-items:center;justify-content:center;margin-bottom:20px}
.card h3{font-size:14px;line-height:16px;font-weight:700;margin-bottom:8px}
.card p{font-size:11px;line-height:18.5px;color:var(--muted)}

/* conference */
.conference{height:482px;background:var(--warm)}
.conference .photo{position:absolute;top:88px;left:0;width:447px;height:307px;border-radius:6px;background:linear-gradient(170deg,#eeece8 0%,#d3cfc9 55%,#a98a66 100%);box-shadow:0 14px 34px rgba(0,0,0,.12)}
.conference .copy{position:absolute;top:70px;left:493px;width:411px}
.conference h2{font-size:44px;line-height:49px;font-weight:700;margin:14px 0 16px}
.conference p{font-size:11.5px;line-height:20px;color:var(--body);margin-bottom:16px}
.checks li{list-style:none;display:flex;align-items:center;gap:8px;font-size:11px;font-weight:700;margin-bottom:10px}
.checks li::before{content:"";width:12px;height:12px;border-radius:50%;background:var(--red)}

/* clients */
.clients{height:730px}
.clients .eyebrow{position:absolute;top:73px;width:100%}
.clients h2{position:absolute;top:93px;width:100%;font-size:44px;line-height:49px;font-weight:700}
.client-grid{position:absolute;top:279px;left:0;width:904px;display:grid;grid-template-columns:1fr 1fr;gap:18px}
.client{border:1px solid var(--line);border-radius:6px;overflow:hidden;height:380px;background:#fff}
.client .photo{height:277px}
.client .photo.office{background:linear-gradient(135deg,#e9e8e6,#f6f5f3 50%,#c9c6c2)}
.client .photo.warehouse{background:linear-gradient(135deg,#ecebe9,#d8cbb7 50%,#b8b4ae)}
.client .body{padding:20px 20px}
.client h3{font-size:14px;font-weight:700;margin-bottom:6px}
.client p{font-size:11px;line-height:19px;color:var(--muted);width:380px}

/* process */
.process{height:467px;background:var(--warm)}
.process .eyebrow{position:absolute;top:72px;left:0}
.process h2{position:absolute;top:93px;left:0;width:370px;font-size:44px;line-height:49px;font-weight:700}
.process .note{position:absolute;top:308px;left:0;width:340px;font-size:11px;line-height:19.5px;color:var(--body)}
.steps{position:absolute;top:74px;left:390px;width:514px;display:grid;grid-template-columns:1fr 1fr;gap:19px 15px}
.step{background:#fff;border:1px solid var(--line);border-radius:6px;height:150px;padding:18px 18px}
.step .num{font-size:9px;font-weight:700;color:var(--red)}
.step h3{font-size:13px;font-weight:700;margin:12px 0 10px}
.step p{font-size:10.5px;line-height:19px;color:var(--muted)}

/* about */
.about{height:425px;border-bottom:1px solid var(--line)}
.about .eyebrow{position:absolute;top:74px;left:0}
.about h2{position:absolute;top:96px;left:0;width:360px;font-size:44px;line-height:49px;font-weight:700}
.about .text{position:absolute;top:72px;left:409px;width:495px;font-size:11.5px;line-height:20px;color:var(--body)}
.stats{position:absolute;top:169px;left:409px;width:495px;display:grid;grid-template-columns:repeat(3,1fr);gap:10px}
.stat{border:1px solid var(--line);border-radius:6px;height:70px;padding:14px 15px}
.stat b{display:block;font-family:"Archivo",sans-serif;font-size:18px;color:var(--red);font-weight:700;line-height:20px}
.stat span{font-size:9.5px;font-weight:600;color:var(--muted)}

/* contact */
.contact{height:645px}
.contact .eyebrow{position:absolute;top:74px;left:0}
.contact h2{position:absolute;top:96px;left:0;width:350px;font-size:44px;line-height:49px;font-weight:700}
.contact .intro{position:absolute;top:266px;left:0;width:350px;font-size:11px;line-height:19px;color:var(--body)}
.offices{position:absolute;top:320px;left:0;font-size:11px;line-height:19px}
.offices dt{font-weight:700;margin-top:16px}
.offices dt:first-child{margin-top:0}
.offices dd{color:var(--body)}
.offices .accent{color:var(--red);font-weight:700}
.quote-form{position:absolute;top:69px;left:415px;width:489px;height:383px;background:#fff;border-top:4px solid var(--red);border-radius:6px;box-shadow:0 14px 40px rgba(0,0,0,.10);padding:26px 24px}
.row{display:grid;grid-template-columns:1fr 1fr;gap:14px;margin-bottom:18px}
.field label{display:block;font-size:9.5px;font-weight:700;margin-bottom:8px}
.input{height:37px;border:1px solid var(--line);border-radius:4px;font-size:10.5px;font-weight:600;display:flex;align-items:center;justify-content:space-between;padding:0 12px}
.textarea{height:111px;border:1px solid var(--line);border-radius:4px}
.quote-form .btn{margin-top:16px;height:36px}

/* footer */
.site-footer{height:226px;background:var(--warm)}
.site-footer .brand{position:absolute;top:36px;left:0;font-size:30px}
.site-footer .brand .mark{width:30px;height:30px}
.site-footer .tagline{position:absolute;top:93px;left:0;width:310px;font-size:11px;line-height:19px;color:var(--body)}
.foot-links{position:absolute;top:37px;left:665px;font-size:11px;font-weight:700;line-height:28px;list-style:none}
.foot-contact{position:absolute;top:37px;left:764px;font-size:11px;font-weight:700;line-height:28px;list-style:none}
.foot-contact .tel{color:var(--red)}
.legal{position:absolute;top:190px;left:0;width:904px;border-top:1px solid var(--line);padding-top:12px;display:flex;justify-content:space-between;font-size:9.5px;color:var(--muted)}
</style>
</head>
<body>

<header class="site-header">
  <div class="wrap">
    <div class="brand"><span class="mark"></span>Wirenexa</div>
    <nav class="nav"><span>Services</span><span>Markets</span><span>About</span><span>Contact</span><span class="tel">(888) 555-0147</span></nav>
  </div>
</header>

<section class="hero">
  <div class="wrap">
    <div class="eyebrow">Commercial low voltage specialists</div>
    <h1>Structured cabling and connected systems for offices and warehouses.</h1>
    <p class="lede">Wirenexa designs and installs clean, professional infrastructure for Wi-Fi, conference rooms, access control, CCTV, POS, Skyreach, copper, and fiber projects across Virginia, Washington DC, and Maryland.</p>
    <div class="actions">
      <span class="btn primary"><svg width="12" height="12" viewBox="0 0 24 24" fill="none" stroke="#fff" stroke-width="2.4"><path d="M5 3h4l2 5-3 2a12 12 0 0 0 6 6l2-3 5 2v4a2 2 0 0 1-2 2A17 17 0 0 1 3 5a2 2 0 0 1 2-2z"/></svg>Request a quote</span>
      <span class="btn ghost">View services</span>
    </div>
    <div class="tags"><span class="tag">Since 1994</span><span class="tag">Commercial projects</span><span class="tag">Copper &amp; fiber</span></div>
    <div class="photo" role="img" aria-label="Bright office corridor with glass partitions and a cabling rack in the foreground"></div>
  </div>
</section>

<section class="strip">
  <div class="wrap">
    <div class="cell"><h4>Built for small and mid-size businesses</h4><p>Office buildouts, relocations, warehouse connectivity, and technology upgrades.</p></div>
    <div class="cell"><h4>Designed to be easy to manage</h4><p>Neat terminations, labels, documentation, and room to grow.</p></div>
    <div class="cell"><h4>Installed around your operations</h4><p>Practical planning for active commercial spaces and phased projects.</p></div>
  </div>
</section>

<section class="services center">
  <div class="wrap">
    <div class="eyebrow">What we do</div>
    <h2>Low voltage systems<br>that make commercial<br>spaces work.</h2>
    <p class="intro">A focused service lineup for companies that need reliable connectivity, security, and meeting-room technology without a cluttered process.</p>
    <div class="grid4" style="text-align:left">
      <div class="card"><div class="icon"><svg width="12" height="12" viewBox="0 0 24 24" fill="none" stroke="#d8322c" stroke-width="2.4"><rect x="3" y="4" width="18" height="12" rx="1"/><path d="M9 20h6M12 16v4"/></svg></div><h3>Structured Cabling</h3><p>CAT6, CAT6A, patch panels, racks, MDF/IDF buildouts, labels, and clean cable management.</p></div>
      <div class="card"><div class="icon"><svg width="12" height="12" viewBox="0 0 24 24" fill="none" stroke="#d8322c" stroke-width="2.4"><path d="M2 9a15 15 0 0 1 20 0M5 13a10 10 0 0 1 14 0M9 17a4 4 0 0 1 6 0"/></svg></div><h3>Wi-Fi &amp; WAP</h3><p>Wireless access point placement, cabling, mounting, and coverage planning for office and warehouse spaces.</p></div>
      <div class="card"><div class="icon"><svg width="12" height="12" viewBox="0 0 24 24" fill="none" stroke="#d8322c" stroke-width="2.4"><rect x="3" y="7" width="13" height="9" rx="1"/><path d="M16 10l5-3v9l-5-3"/></svg></div><h3>CCTV &amp; Video Surveillance</h3><p>Camera cabling, device placement, recorder connectivity, and tidy installs for commercial visibility.</p></div>
      <div class="card"><div class="icon"><svg width="12" height="12" viewBox="0 0 24 24" fill="none" stroke="#d8322c" stroke-width="2.4"><rect x="5" y="11" width="14" height="10" rx="1"/><path d="M8 11V7a4 4 0 0 1 8 0v4"/></svg></div><h3>Access Control</h3><p>Door controllers, card readers, low-voltage pathways, and entry systems for commercial suites.</p></div>
      <div class="card"><div class="icon"><svg width="12" height="12" viewBox="0 0 24 24" fill="none" stroke="#d8322c" stroke-width="2.4"><rect x="3" y="4" width="18" height="12" rx="1"/><path d="M12 16v5"/></svg></div><h3>Conference Rooms</h3><p>Display, camera, microphone, speaker, control, and table connectivity for clear meetings.</p></div>
      <div class="card"><div class="icon"><svg width="12" height="12" viewBox="0 0 24 24" fill="none" stroke="#d8322c" stroke-width="2.4"><rect x="3" y="5" width="18" height="14" rx="1"/><path d="M3 10h18"/></svg></div><h3>POS &amp; Skyreach</h3><p>Point-of-sale network drops, payment station cabling, Skyreach mounting support, and backhaul connectivity.</p></div>
      <div class="card"><div class="icon"><svg width="12" height="12" viewBox="0 0 24 24" fill="none" stroke="#d8322c" stroke-width="2.4"><path d="M3 12h18M15 6l6 6-6 6"/></svg></div><h3>Copper &amp; Fiber</h3><p>Single-mode, multimode, backbone cabling, testing coordination, and documentation-ready installs.</p></div>
      <div class="card"><div class="icon"><svg width="12" height="12" viewBox="0 0 24 24" fill="none" stroke="#d8322c" stroke-width="2.4"><path d="M12 21s-7-7-7-12a7 7 0 0 1 14 0c0 5-7 12-7 12z"/><circle cx="12" cy="9" r="2.5"/></svg></div><h3>Planning &amp; Permits</h3><p>Site walks, project scoping, low-voltage pathways, and practical coordination with building teams.</p></div>
    </div>
  </div>
</section>

<section class="conference">
  <div class="wrap">
    <div class="photo" role="img" aria-label="Modern conference room with a wall display, long wooden table and chairs"></div>
    <div class="copy">
      <div class="eyebrow dark">Conference room technology</div>
      <h2>Clean rooms,<br>clear calls, fewer<br>loose ends.</h2>
      <p>From displays and cameras to speakers, microphones, control panels, and table connectivity, Wirenexa helps commercial teams create meeting rooms that are simple to use and easy to support.</p>
      <ul class="checks"><li>Display and camera cabling</li><li>Ceiling speakers and microphones</li><li>Network drops for control and AV hardware</li></ul>
    </div>
  </div>
</section>

<section class="clients center">
  <div class="wrap">
    <div class="eyebrow">Commercial clients</div>
    <h2>Focused on offices,<br>warehouses, and active<br>business spaces.</h2>
    <div class="client-grid" style="text-align:left">
      <div class="client"><div class="photo office" role="img" aria-label="Office entry with glass doors, a card reader and a ceiling camera"></div><div class="body"><h3>Office Buildings</h3><p>Tenant improvements, network closets, access control, CCTV, conference rooms, and Wi-Fi buildouts.</p></div></div>
      <div class="client"><div class="photo warehouse" role="img" aria-label="Warehouse with stocked shelving, a wall network cabinet and a POS station"></div><div class="body"><h3>Warehouses</h3><p>WAP coverage, rack and patch panel organization, POS/scanner stations, and practical cable pathways.</p></div></div>
    </div>
  </div>
</section>

<section class="process">
  <div class="wrap">
    <div class="eyebrow dark">How projects run</div>
    <h2>Structured from the first walkthrough to final labeling.</h2>
    <p class="note">The site should reassure business owners and facility managers that Wirenexa understands real commercial constraints: timing, clean installation, coordination, and future support.</p>
    <div class="steps">
      <div class="step"><div class="num">01</div><h3>Walkthrough</h3><p>Review the space, users, systems, pathways, device locations, and growth requirements.</p></div>
      <div class="step"><div class="num">02</div><h3>Scope</h3><p>Define cabling, racks, access points, cameras, readers, conference room gear, and scheduling needs.</p></div>
      <div class="step"><div class="num">03</div><h3>Install</h3><p>Execute cleanly with commercial-grade workmanship, practical coordination, and minimal disruption.</p></div>
      <div class="step"><div class="num">04</div><h3>Label</h3><p>Close with labeling, documentation, testing coordination, and a system your team can understand.</p></div>
    </div>
  </div>
</section>

<section class="about">
  <div class="wrap">
    <div class="eyebrow dark">About Wirenexa</div>
    <h2>A local low voltage partner for commercial technology projects.</h2>
    <p class="text">Wirenexa supports small and mid-size businesses with practical, well-organized infrastructure work. The new site positions the company around commercial offices and warehouses, with a cleaner message and no residential or industrial service emphasis.</p>
    <div class="stats">
      <div class="stat"><b>1994</b><span>Company founded</span></div>
      <div class="stat"><b>VA/DC/MD</b><span>Core service area</span></div>
      <div class="stat"><b>B2B</b><span>Commercial focus</span></div>
    </div>
  </div>
</section>

<section class="contact">
  <div class="wrap">
    <div class="eyebrow dark">Request a quote</div>
    <h2>Tell us what your business space needs.</h2>
    <p class="intro">Share a few details about the project and Wirenexa can follow up with the right next step.</p>
    <dl class="offices">
      <dt>Main office</dt><dd>4120 Meridian Pkwy, Suite 210<br>Fairfax, VA 22031</dd>
      <dt>Regional office</dt><dd>1850 Harbor Point Dr, Suite 300<br>Rockville, MD 20852</dd>
      <dt>Email</dt><dd class="accent">sales@wirenexa.com</dd>
      <dt>Phone</dt><dd class="accent">(888) 555-0147</dd>
    </dl>
    <div class="quote-form">
      <div class="row"><div class="field"><label>Name</label><div class="input"></div></div><div class="field"><label>Email</label><div class="input"></div></div></div>
      <div class="row"><div class="field"><label>Phone</label><div class="input"></div></div><div class="field"><label>Project type</label><div class="input">Structured cabling<svg width="9" height="9" viewBox="0 0 24 24" fill="none" stroke="#141414" stroke-width="3"><path d="M6 9l6 6 6-6"/></svg></div></div></div>
      <div class="field"><label>Project details</label><div class="textarea"></div></div>
      <span class="btn primary">Send request</span>
    </div>
  </div>
</section>

<footer class="site-footer">
  <div class="wrap">
    <div class="brand"><span class="mark"></span>Wirenexa</div>
    <p class="tagline">Commercial low voltage cabling and connected technology systems for offices and warehouses.</p>
    <ul class="foot-links"><li>Services</li><li>Markets</li><li>About</li><li>Contact</li></ul>
    <ul class="foot-contact"><li class="tel">(888) 555-0147</li><li>sales@wirenexa.com</li></ul>
    <div class="legal"><span>Copyright © 2026 Wirenexa</span><span>Website redesign concept</span></div>
  </div>
</footer>

</body>
</html>
```